Delivery Docket urgent plus require many other designs for more stationary after this.

We need a new delivery docket design urgently as the one we have needs updating and we have changed our company name. Please do not copy the one I have uploaded as we do not feel this looks professional enough. I uploaded it as a few designers requested to see what we are currently using thank you.
It is quite complex in that we need a range of information to be on the one docket.
We are a Transport Company based in Australia that has a wide variety of items that we deliver such as water, sand and gravels and heavy equipment transport.
We would prefer to keep this design to A5 size as we will get them made into books. We are looking for a modern professional look. Although it is only a delivery docket this is given to all our customers so needs to look impressive.

We need our new logo on the docket (PRW). There will also need to be areas for our address and contact numbers, email etc these will be supplied to the winning designer to make the final adjustments so for now just put something generic in these spaces.
Needs to have an area for customer details, purchase order number, date and docket number (docket number to be in red)
Needs a section where we can list the type of product / and or service that has been provided and the amount / qty usually 3 lines will be enough for this. Need area under this where the customer can sign name and print name to say that the goods / and or services have been received.

Also required somewhere on the docket are the words, Tax Invoice will be issued based on the information provided on this docket. Conditions on back of page

We then need a separate section on the same page which we will use internally that the staff member can tear off and hand into the office. On this section it needs to have area where the driver can list km at start of job and at end with space to calculate km travelled, details of fuel purchased eg amount and litres, vehicle that is being used. also need to log down wheel bearing temps.
prime mover needs spaces as follows
Steer axel FL____________ Steer axel FR _________ 1st drive axel L_______
1st drive axel R_________ 2nd drive axel L_______ 2nd drive axel R________

For the trailers need something similar x 2 as have 2 trailers
1st axel DS_________ 1st axel PS_________ 2nd axel DS__________
2nd axel PS_________ 3rd axel DS_________ 3rd axel PS__________

I have included a few examples of designs we have used in past and ones that we like so you can get an idea of the colours we prefer, I have included some of the designs we are currently receiving for our logo that I like so you can get idea again of colours we prefer. There is much more we need designed also such as time sheets, more delivery dockets and letter heads so there is a lot of more work available to the winning designer.

Thank you

Target Market(s)

Customers

Font styles to use
Serif
Sans Serif

Colors

Designer to choose colors to be used in the design.

Requirements
Should not have
• Please don't copy old docket as we do not like it and nned new info on new design thank you

```html
<!DOCTYPE html>
<html lang="en">
<head>
<meta charset="utf-8">
<title>PRW Delivery Docket</title>
<link href="https://fonts.googleapis.com/css2?family=Poppins:wght@400;500;600&display=swap" rel="stylesheet">
<style>
:root{
  --ink:#111;
  --black:#050505;
  --red:#ee1c24;
  --grey-dark:#666;
  --grey-mid:#9a9a9a;
  --panel:#f5f5f5;
  --panel-cool:#eef0ef;
  --line:#222;
  --white:#fff;
}
*{box-sizing:border-box;margin:0;padding:0}
html,body{width:1200px;height:873px;overflow:hidden;background:#fff}
body{font-family:'Poppins',sans-serif;color:var(--ink)}
.docket{position:relative;width:1200px;height:873px;border:3px solid #2a2a2a;background:var(--white)}
.abs{position:absolute}
.contact-bar{left:233px;top:9px;width:464px;height:100px;background:var(--black);color:#fff;display:flex;align-items:center}
.contact-item{flex:1;text-align:center;font-size:11px;line-height:16px;position:relative;padding-top:30px;height:100%;display:flex;flex-direction:column;justify-content:center}
.contact-item svg{position:absolute;top:10px;left:50%;transform:translateX(-50%)}
.contact-item+.contact-item{border-left:1px solid #555}
.docket-no{left:705px;top:9px;width:270px;height:48px;background:var(--red);color:#fff;font-size:14px;font-weight:500;display:flex;align-items:center;padding-left:7px;clip-path:polygon(0 0,88% 0,100% 100%,0 100%);letter-spacing:.3px}
.date-label{left:975px;top:21px;font-size:11px;font-weight:500}
.date-boxes{left:1015px;top:20px;display:flex}
.date-boxes span{width:20px;height:19px;border:1px solid #555;font-size:10px;color:#aaa;text-align:center;line-height:17px;margin-right:-1px}
.date-boxes span:nth-child(2n){margin-right:1px}
.po-bar{left:705px;top:63px;width:475px;height:45px;background:var(--grey-dark);color:#fff;font-size:13px;font-weight:500;display:flex;align-items:center;padding-left:10px}
.tab{left:15px;top:122px;width:203px;height:30px;background:var(--black);color:#fff;font-size:13px;font-weight:600;letter-spacing:.8px;display:flex;align-items:center;padding-left:7px;clip-path:polygon(0 0,89% 0,100% 100%,0 100%)}
.panel{background:var(--panel)}
.customer{left:15px;top:151px;width:1168px;height:124px}
.field-row{position:absolute;left:13px;right:10px;display:flex;align-items:flex-end;gap:6px;font-size:14px;font-weight:500}
.field-row .line{flex:1;border-bottom:1px solid var(--line);height:1px;margin-bottom:4px}
.products-head{left:15px;top:277px;width:1168px;height:30px;background:var(--grey-dark);color:#fff;font-size:13px;font-weight:500;display:flex;align-items:center;justify-content:space-between;padding:0 95px 0 10px}
.products{left:15px;top:307px;width:1168px;height:152px}
.product-line{position:absolute;left:13px;right:10px;border-bottom:1px solid var(--line)}
.divider{position:absolute;left:875px;top:0;height:97px;border-left:2px solid #777}
.tax-note{position:absolute;left:0;right:0;top:117px;text-align:center;font-size:13px}
.receipt{left:15px;top:469px;width:1168px;height:68px;border:2px solid #999;display:flex}
.receipt .lbl{background:var(--grey-mid);color:#fff;font-size:12px;font-weight:500;letter-spacing:.5px;display:flex;align-items:center;justify-content:center;text-align:center;line-height:19px}
.cut{left:15px;top:546px;width:1168px;height:16px}
.office{left:15px;top:581px;width:1168px;height:106px}
.section-title{position:absolute;left:0;right:0;display:flex;align-items:center;gap:14px}
.section-title::before,.section-title::after{content:"";flex:1;border-top:1.5px solid var(--line)}
.office .section-title{top:14px;font-size:17px;font-weight:500;letter-spacing:.5px}
.km-row{position:absolute;left:11px;right:14px;top:64px;display:flex;align-items:flex-end;font-size:11.5px}
.km-row .val{border-bottom:1px solid var(--line);font-size:10px;color:#666;padding:0 10px 1px;margin:0 20px 0 10px}
.bearings{left:15px;top:697px;width:1168px;height:156px;background:var(--panel-cool)}
.bearings .section-title{top:20px;font-size:12px;font-weight:600;letter-spacing:1px}
.checks{position:absolute;left:14px;top:46px;display:flex;gap:22px;font-size:11.5px}
.checks label{display:flex;align-items:center;gap:8px}
.checks i{width:18px;height:18px;border:2px solid #222;display:inline-block}
.temp{position:absolute;display:flex;align-items:flex-end;font-size:11.5px}
.temp .line{width:72px;border-bottom:1px solid var(--line);margin-left:12px;margin-bottom:3px}
</style>
</head>
<body>
<div class="docket">

  <div class="abs contact-bar">
    <div class="contact-item">
      <svg width="28" height="28" viewBox="0 0 28 28"><circle cx="14" cy="14" r="12.5" fill="none" stroke="#fff" stroke-width="1.5"/><path d="M14 7a4.5 4.5 0 0 0-4.5 4.5C9.5 15 14 20 14 20s4.5-5 4.5-8.5A4.5 4.5 0 0 0 14 7z" fill="#fff"/><circle cx="14" cy="11.5" r="1.6" fill="#050505"/></svg>
      <span>12 HARBOUR ST NORTHVALE</span><span>Q 4100, SYDNEY, AUSTRALIA</span>
    </div>
    <div class="contact-item">
      <svg width="28" height="28" viewBox="0 0 28 28"><circle cx="14" cy="14" r="12.5" fill="none" stroke="#fff" stroke-width="1.5"/><path d="M10 8.5l2 -.5 1.3 3-1.3 1c.7 1.5 1.8 2.6 3.3 3.3l1-1.3 3 1.3-.5 2c-4.5.3-9-4.2-8.8-8.8z" fill="#fff"/></svg>
      <span>0400 123 456</span><span>0400 654 321</span>
    </div>
    <div class="contact-item">
      <svg width="28" height="28" viewBox="0 0 28 28"><circle cx="14" cy="14" r="12.5" fill="none" stroke="#fff" stroke-width="1.5"/><g fill="none" stroke="#fff" stroke-width="1.2"><circle cx="14" cy="14" r="6"/><ellipse cx="14" cy="14" rx="2.6" ry="6"/><path d="M8 14h12M9 11h10M9 17h10"/></g></svg>
      <span>INFO@PRW.COM.AU</span><span>WWW.PRW.COM.AU</span>
    </div>
  </div>

  <div class="abs docket-no">DELIVERY DOCKET NO: <span style="font-weight:400;margin-left:4px">20512</span></div>
  <div class="abs date-label">DATE:</div>
  <div class="abs date-boxes"><span>D</span><span>D</span><span>M</span><span>M</span><span>Y</span><span>Y</span><span>Y</span><span>Y</span></div>
  <div class="abs po-bar">PURCHASE ORDER NO: <span style="font-weight:400;margin-left:4px">201234</span></div>

  <div class="abs tab">CUSTOMER DETAILS</div>
  <div class="abs panel customer">
    <div class="field-row" style="top:10px"><span>Name</span><span class="line" style="flex:6"></span><span style="margin-left:6px">Phone</span><span class="line" style="flex:2.2"></span><span style="margin-left:4px">Email</span><span class="line" style="flex:3.1"></span></div>
    <div class="field-row" style="top:46px"><span>Address</span><span class="line"></span></div>
    <div class="field-row" style="top:82px"><span>City</span><span class="line" style="flex:4.6"></span><span style="margin-left:8px">State</span><span class="line" style="flex:4"></span><span style="margin-left:12px">Zip</span><span class="line" style="flex:1.4"></span></div>
  </div>

  <div class="abs products-head"><span>PRODUCT / SERVICES</span><span>AMOUNT/ QTY</span></div>
  <div class="abs panel products">
    <div class="divider"></div>
    <div class="product-line" style="top:29px"></div>
    <div class="product-line" style="top:64px"></div>
    <div class="product-line" style="top:98px"></div>
    <p class="tax-note">*** Tax Invoice will be issued based on the information provided on this docket. Conditions on back of page ***</p>
  </div>

  <div class="abs receipt">
    <div class="lbl" style="width:186px">GOODS RECEIVED BY<br>(PRINT NAME)</div>
    <div style="width:314px"></div>
    <div class="lbl" style="width:140px">CUSTOMER<br>SIGNATURE</div>
    <div style="width:219px"></div>
    <div class="lbl" style="width:105px;justify-content:flex-start;padding-left:18px;text-align:left">DATE OF<br>RECEIVING</div>
    <div style="flex:1"></div>
  </div>

  <svg class="abs cut" viewBox="0 0 1168 16">
    <line x1="0" y1="8" x2="1168" y2="8" stroke="#111" stroke-width="1.8" stroke-dasharray="6 5"/>
    <g id="scissors" fill="none" stroke="#111" stroke-width="1.6">
      <rect x="-10" y="-8" width="20" height="16" fill="#fff" stroke="none"/>
      <circle cx="-5" cy="-4" r="2.6"/><circle cx="-5" cy="4" r="2.6"/>
      <path d="M-2.5 -2.5L8 5M-2.5 2.5L8 -5"/>
    </g>
    <use href="#scissors" x="98" y="8"/>
    <use href="#scissors" x="436" y="8"/>
    <use href="#scissors" x="775" y="8"/>
    <use href="#scissors" x="1112" y="8"/>
  </svg>

  <div class="abs panel office">
    <div class="section-title">FOR OFFICE USE ONLY</div>
    <div class="km-row">
      <span>Starting Point(km)</span><span class="val">27450</span>
      <span>Destination Point(km)</span><span class="val">28190</span>
      <span>Distance Travelled(km)</span><span class="val">840</span>
      <span>Fuel Used(Lt)</span><span class="val">84</span>
      <span>Amount($)</span><span class="val">2560.00</span>
      <span>Vehhicle</span><span class="val" style="flex:1;margin-right:0">Ridgeline Hauler 14 wheel</span>
    </div>
  </div>

  <div class="abs bearings">
    <div class="section-title">LOG DOWN WHEEL BEARING TEMPS</div>
    <div class="checks"><label><i></i>Prime Movers</label><label><i></i>Trailers</label></div>
    <div class="temp" style="left:13px;top:80px">Steer axel FL<span class="line"></span></div>
    <div class="temp" style="left:192px;top:80px">Steer axel FR<span class="line"></span></div>
    <div class="temp" style="left:376px;top:80px">1st drive axel L<span class="line"></span></div>
    <div class="temp" style="left:643px;top:80px">1st axel DS<span class="line"></span></div>
    <div class="temp" style="left:821px;top:80px">1st axel PS<span class="line"></span></div>
    <div class="temp" style="left:1005px;top:80px">2nd axel DS<span class="line"></span></div>
    <div class="temp" style="left:13px;top:119px">1st drive axel R<span class="line"></span></div>
    <div class="temp" style="left:192px;top:119px">2nd drive axel L<span class="line"></span></div>
    <div class="temp" style="left:376px;top:119px">2nd drive axel R<span class="line"></span></div>
    <div class="temp" style="left:643px;top:119px">2nd axel PS<span class="line"></span></div>
    <div class="temp" style="left:821px;top:119px">3rd axel DS<span class="line"></span></div>
    <div class="temp" style="left:1005px;top:119px">3rd axel PS<span class="line"></span></div>
  </div>

</div>
</body>
</html>
```